M Zyvantics Buisness Cards

I need a technology focused clean business card for my employees. I have attached out logo to include in the mocks. We're a modern tech consulting firm that drives to interface humanity with technology in a truly cohesive fashion.

```html
<!DOCTYPE html>
<html lang="en">
<head>
<meta charset="utf-8">
<title>M Zyvantics Business Cards</title>
<link href="https://fonts.googleapis.com/css2?family=Exo+2:wght@400;500;600;700&display=swap" rel="stylesheet">
<style>
  :root {
    --backdrop: #3a3f46;
    --brand-blue: #1f78c4;
    --card-white: #ffffff;
    --card-black: #0d0d0e;
    --silver: #b9bcc0;
    --text-light: #ffffff;
  }
  * { margin: 0; padding: 0; box-sizing: border-box; }
  html, body { width: 1200px; height: 900px; overflow: hidden; }
  body {
    background: var(--backdrop);
    font-family: "Exo 2", sans-serif;
    position: relative;
  }
  .card {
    position: absolute;
    width: 540px;
    height: 309px;
    border-radius: 4px;
    overflow: hidden;
    box-shadow: 0 14px 30px rgba(0,0,0,0.45);
  }
  .card-front { left: 40px; top: 296px; background: var(--brand-blue); }
  .card-back { left: 620px; top: 296px; background: var(--card-black); }

  .front-shape { position: absolute; inset: 0; }

  .contact-block {
    position: absolute;
    left: 26px;
    top: 28px;
    width: 222px;
    color: var(--text-light);
  }
  .person-name { font-size: 23px; font-weight: 600; letter-spacing: 0.4px; line-height: 1.15; }
  .person-role { font-size: 13px; font-weight: 400; margin-bottom: 20px; }
  .address { font-size: 12.5px; line-height: 1.4; margin-bottom: 8px; }
  .contact-line {
    display: flex; align-items: center; gap: 7px;
    font-size: 12.5px; line-height: 1.5;
  }
  .contact-line svg { width: 10px; height: 10px; flex: none; }

  .front-brand {
    position: absolute;
    left: 270px; top: 172px;
    width: 260px;
    text-align: center;
    font-size: 28px;
    font-weight: 700;
    color: var(--brand-blue);
  }

  .back-brand {
    position: absolute;
    left: 44px; top: 58px;
    font-size: 40px;
    font-weight: 600;
    color: var(--silver);
    letter-spacing: 1px;
  }
</style>
</head>
<body>

  <section class="card card-front" aria-label="Business card front">
    <svg class="front-shape" viewBox="0 0 540 309" aria-hidden="true">
      <circle cx="400" cy="192" r="148" fill="var(--card-white)"/>
      <rect x="400" y="0" width="140" height="309" fill="var(--card-white)"/>
    </svg>

    <div class="contact-block">
      <h1 class="person-name">Daniel Moreno</h1>
      <p class="person-role">Managing Director</p>
      <p class="address">415 Harbor Loop, Suite 210<br>Cary, NC 27511</p>
      <p class="contact-line">
        <svg viewBox="0 0 10 10"><path d="M2 0.5 L3.6 2.6 L2.8 3.6 Q4 6 6.4 7.2 L7.4 6.4 L9.5 8 L8.3 9.5 Q1 8 0.5 1.7 Z" fill="currentColor"/></svg>
        919.555.0142
      </p>
      <p class="contact-line">
        <svg viewBox="0 0 10 10"><rect x="2" y="0.5" width="6" height="3" fill="currentColor"/><rect x="0.5" y="3.5" width="9" height="4" rx="1" fill="currentColor"/><rect x="2" y="7" width="6" height="2.5" fill="currentColor"/></svg>
        919.555.0187
      </p>
      <p class="contact-line">
        <svg viewBox="0 0 10 10"><rect x="0.5" y="1.5" width="9" height="7" fill="currentColor"/><path d="M0.5 1.5 L5 5.5 L9.5 1.5" stroke="var(--brand-blue)" stroke-width="1" fill="none"/></svg>
        daniel@mzyvantics.com
      </p>
      <p class="contact-line">
        <svg viewBox="0 0 10 10"><circle cx="5" cy="5" r="4.3" fill="none" stroke="currentColor" stroke-width="1"/><ellipse cx="5" cy="5" rx="1.8" ry="4.3" fill="none" stroke="currentColor" stroke-width="0.8"/><line x1="0.7" y1="5" x2="9.3" y2="5" stroke="currentColor" stroke-width="0.8"/></svg>
        www.mzyvantics.com
      </p>
    </div>

    <p class="front-brand">M Zyvantics</p>
  </section>

  <section class="card card-back" aria-label="Business card back">
    <p class="back-brand">M Zyvantics</p>
  </section>

</body>
</html>
```